DOUBLE SIDED BROCHURE NEEDED TO PROMOTE DOCTOR

I need a double sided DL size (99mm x 210mm) brochure, promoting a doctor seeing patients in a new area.

I want something professional. I have included the relevant information. I would also like the Dr's picture somwhere in the brochure, with a professional background. I wish to print these tomorrow, so i will pick a winner within 14 hours of posting this ad.

I have included an example of a brochures design that I recently saw, and its definietly a good starting point.

Medical

```html
<!DOCTYPE html>
<html lang="en">
<head>
<meta charset="utf-8">
<title>Dr. Samir Haddad – DL Referral Brochure</title>
<link rel="stylesheet" href="https://fonts.googleapis.com/css2?family=Marcellus+SC&family=Alegreya+Sans:ital,wght@0,400;0,500;1,400&display=swap">
<style>
  :root{
    --navy:#0b2a5c;
    --navy-deep:#071d44;
    --blue:#1f6fc4;
    --sky:#2b8fe0;
    --silver:#b9bec6;
    --paper:#ffffff;
    --page:#e7e8ea;
    --ink:#14234a;
  }
  *{box-sizing:border-box;margin:0;padding:0}
  html,body{width:849px;height:1200px;overflow:hidden;background:var(--page)}
  .sheet{position:relative;width:849px;height:1200px}
  .panel{position:absolute;top:180px;width:396px;height:840px;background:var(--paper);overflow:hidden;box-shadow:0 2px 10px rgba(0,0,0,.15)}
  .panel--back{left:18px}
  .panel--front{left:435px}
  .panel svg.decor{position:absolute;inset:0;width:100%;height:100%}

  /* back side */
  .letter{position:absolute;left:26px;right:22px;top:86px;font-family:"Alegreya Sans",sans-serif;color:var(--ink)}
  .letter__greeting{font-family:"Marcellus SC",serif;color:var(--blue);font-size:22px;margin-bottom:8px}
  .letter__body{font-size:15.5px;line-height:1.38;text-align:justify}
  .letter__headline{font-family:"Marcellus SC",serif;color:var(--blue);font-size:20.5px;line-height:1.28;margin:26px 0 18px}
  .services{list-style:none;font-family:"Marcellus SC",serif;font-size:18px;color:var(--ink)}
  .services li{display:flex;align-items:flex-start;gap:8px;margin-bottom:12px}
  .services svg{flex:none;width:16px;height:16px;margin-top:4px}
  .services small{display:block;font-family:"Alegreya Sans",sans-serif;font-size:13px;font-style:italic}
  .general__intro{font-family:"Marcellus SC",serif;font-size:18px;margin:16px 0 8px}
  .general{list-style:none;font-family:"Marcellus SC",serif;font-size:15px;padding-left:22px}
  .general li{margin-bottom:5px}
  .general li::before{content:"\2022";margin-right:8px;color:var(--navy)}

  /* front side */
  .title{position:absolute;left:14px;top:28px;font-family:"Marcellus SC",serif;line-height:1.15;text-shadow:1px 2px 3px rgba(0,0,0,.25)}
  .title__lead{display:block;font-size:29px;color:var(--sky)}
  .title__place{display:block;font-size:38px;color:var(--navy);margin-top:4px}
  .photo{position:absolute;left:0;top:150px;width:396px;height:620px;background:linear-gradient(180deg,#7fb2e6 0%,#cfe1f3 40%,#7d8894 70%,#3d4652 100%)}
  .clinic{position:absolute;left:88px;top:690px;font-family:"Alegreya Sans",sans-serif;color:#fff;font-size:17px;line-height:1.15}
  .clinic__label{font-family:"Marcellus SC",serif;font-size:18px;margin-bottom:10px;color:#e6ecf5}
  .referral{position:absolute;left:10px;right:8px;bottom:14px;font-family:"Alegreya Sans",sans-serif;color:#fff;font-size:14.5px;text-align:center}
</style>
</head>
<body>
<main class="sheet">

  <section class="panel panel--back" aria-label="Brochure back: letter to referring doctors">
    <svg class="decor" viewBox="0 0 396 840" preserveAspectRatio="none" aria-hidden="true">
      <path d="M0 95 C120 40 260 30 396 20 L396 0 L0 0 Z" fill="#f1f2f4"/>
      <path d="M0 95 C120 40 260 30 396 22" fill="none" stroke="var(--blue)" stroke-width="7"/>
      <path d="M0 82 C120 32 260 20 396 10" fill="none" stroke="var(--silver)" stroke-width="4"/>
      <path d="M0 840 L0 800 C120 790 260 770 396 735 L396 840 Z" fill="var(--navy)"/>
      <path d="M0 795 C120 784 260 764 396 728" fill="none" stroke="var(--silver)" stroke-width="4"/>
    </svg>
    <div class="letter">
      <h2 class="letter__greeting">Dear Doctors,</h2>
      <p class="letter__body">We are pleased to announce that Dr. Samir Haddad is now consulting in Mandurah, seeing public and private patients.<br>
      Guaranteed appointment within two weeks, with patients having the option of surgery at Estuary Health Campus, Southgate General Hospital or St. Clare's Private Murdoch.</p>
      <h3 class="letter__headline">Dr. Haddad is a highly specialised surgeon in the areas of endocrine &amp; general surgery</h3>
      <ul class="services">
        <li><svg viewBox="0 0 16 16"><circle cx="8" cy="8" r="6.5" fill="none" stroke="var(--navy)" stroke-width="1.6"/><path d="M4.8 8.2l2.2 2.1 4.2-4.3" fill="none" stroke="var(--navy)" stroke-width="1.8"/></svg>Thyroid Surgery</li>
        <li><svg viewBox="0 0 16 16"><circle cx="8" cy="8" r="6.5" fill="none" stroke="var(--navy)" stroke-width="1.6"/><path d="M4.8 8.2l2.2 2.1 4.2-4.3" fill="none" stroke="var(--navy)" stroke-width="1.8"/></svg><span>Parathyroid Surgery<small>(including minimally invasive)</small></span></li>
        <li><svg viewBox="0 0 16 16"><circle cx="8" cy="8" r="6.5" fill="none" stroke="var(--navy)" stroke-width="1.6"/><path d="M4.8 8.2l2.2 2.1 4.2-4.3" fill="none" stroke="var(--navy)" stroke-width="1.8"/></svg>Breast Cancer Surgery</li>
      </ul>
      <p class="general__intro">All areas of general surgery including:</p>
      <ul class="general">
        <li>Gallbladder</li>
        <li>Hernia repair</li>
        <li>Haemorrhoids</li>
        <li>Colonoscopy</li>
        <li>Varicose veins</li>
      </ul>
    </div>
  </section>

  <section class="panel panel--front" aria-label="Brochure front cover">
    <div class="photo" role="img" aria-label="Portrait photo of the doctor in front of a modern hospital building under a blue sky"></div>
    <svg class="decor" viewBox="0 0 396 840" preserveAspectRatio="none" aria-hidden="true">
      <path d="M0 0 L396 0 L396 150 C300 140 200 190 120 240 C70 270 30 290 0 300 Z" fill="var(--paper)"/>
      <path d="M0 300 C30 290 70 270 120 240 C200 190 300 140 396 150" fill="none" stroke="var(--blue)" stroke-width="8"/>
      <path d="M0 312 C40 300 90 275 140 245 C220 198 310 156 396 162" fill="none" stroke="var(--silver)" stroke-width="3"/>
      <path d="M0 840 L0 775 C60 730 110 700 170 710 C240 722 280 700 330 670 C360 652 380 648 396 646 L396 840 Z" fill="var(--navy)"/>
      <path d="M0 775 C60 730 110 700 170 710 C240 722 280 700 330 670 C360 652 380 648 396 646" fill="none" stroke="var(--silver)" stroke-width="6"/>
      <path d="M0 840 L0 800 C80 790 200 800 396 770 L396 840 Z" fill="var(--navy-deep)" opacity=".6"/>
    </svg>
    <h1 class="title">
      <span class="title__lead">Dr. Haddad is now<br>consulting in</span>
      <span class="title__place">Mandurah</span>
    </h1>
    <address class="clinic" style="font-style:normal">
      <p class="clinic__label">Mandurah Clinic:</p>
      <p>42 Harbour View Road<br>Mandurah WA 6210.<br>Phone: 1300 555 018</p>
    </address>
    <p class="referral">Please send all referrals by fax to (08) 5550 2184</p>
  </section>

</main>
</body>
</html>
```